Maine Organic farm needs a label design for various food products

We need a label design that we can use across a variety of vegetable-based food products that we produce using some of our organic vegetables that we grow on our farm located in Maine, USA.
Our products include:
1) a Traditional and Vegan Korean Kimchi
2) Pomrak Sauce (a Korean Hot Sauce)
3) Pickles of Brambleton Relish
4) Radishtastic Chutney
5) Seasonal Soups (many varieties, depending on what's available during the season)
6) Iron Oath Maple Syrup (we are retired from the U.S. Harbor Guard, hence the name and spelling)
7) Maine Wild Blueberry Kombucha (made with organic Maine wild blueberries)

For the Korean products (kimchi and Pomrak Sauce) we would like to incorporate the Korean chili pepper (red) and chopsticks. The attached picture was taken from the internet, it has not been trademarked, but I am hesitant to use it as is as our business expands. Would like the "kimchi" to somehow incorporate the chopstick and pepper, but not look exactly like the attached image.

The final design should communicate farm fresh, organic, healthy and high quality ingredients, and Maine-made. All of our products go into glass jars 16oz and 8 oz. The hot sauce goes into 5.5oz and 8 oz bottles, the Maple Syrup goes into 8oz and 16oz bottles, and a 12oz bottle for the Kombucha. We will need the flexibility of changing some components of the label to accommodate each different food product.

The labels do not have the encircle the entirety of the jar. We understand that this is a tall order to fit so many different products. We are hoping that once we get the feel and design down, we can work with you for a fee outside of the competition to finalize other products labels on different sizes jars, bottles, etc. Its most important that we get the right feel for a label that can be used for a wide variety of food products.

Target Market(s)

Health conscious, foodies, local farm supporters

Font styles to use
Serif
Decorative
Script

Colors

Designer to choose colors to be used in the design.

Requirements
Must have
• Fenwick Hollow Farm Logo. Room for product name (interchangeable per product), ingredients list, space for jar size (8 oz, 12 oz, 16 oz). On Korean products -must have Korean hot chili pepper and chopsticks
Nice to have
• We'd like something fairly bold and rustic looking.
Should not have
• Nothing too modern or industrial looking. Nothing hippy-ish. Clean and professional. No cartoonish looking letters or designs.

```html
<!DOCTYPE html>
<html lang="en">
<head>
<meta charset="utf-8">
<title>Fenwick Hollow Farm – Product Label System</title>
<link href="https://fonts.googleapis.com/css2?family=Montserrat:wght@400;500;600;700&family=Oswald:wght@500;600&family=Playfair+Display:wght@800;900&family=Mr+Dafoe&display=swap" rel="stylesheet">
<style>
  :root{
    --backdrop:#d4d1d3;
    --maroon:#6a2226;
    --navy:#13365a;
    --ink:#2a1e18;
    --chili:#d8242a;
    --leaf:#3f8a3a;
    --ribbon-text:#f4e7d5;
  }
  *{box-sizing:border-box}
  html,body{margin:0;padding:0;overflow:hidden}
  body{width:1200px;height:1200px;background:var(--backdrop);position:relative;font-family:"Montserrat",sans-serif}
  .label{position:absolute}
  .label-shape{position:absolute;left:0;top:0;overflow:visible}
  .outline{stroke:var(--maroon);stroke-width:5;stroke-linejoin:round}

  .brand{position:absolute;transform:translateX(-50%);text-align:center;width:160px}
  .brand-dot{display:block;width:24px;height:24px;margin:0 auto 3px;border:2px solid var(--navy);border-radius:50%}
  .brand-name{font-family:"Montserrat",sans-serif;font-weight:700;color:var(--navy);font-size:13px;line-height:1.1;letter-spacing:.4px}

  .nutrition{position:absolute;border:1.5px solid var(--ink);border-radius:5px;padding:5px 6px;color:var(--ink);overflow:hidden}
  .nutrition h3{margin:0 0 3px;font-family:"Oswald",sans-serif;font-weight:600;font-size:15px;line-height:1;letter-spacing:-.4px;white-space:nowrap;border-bottom:2px solid var(--ink);padding-bottom:2px}
  .nf-head{display:flex;font-size:4.5px;line-height:1.2;border-bottom:1.5px solid var(--ink);padding-bottom:2px}
  .nf-head span{flex:1}
  .nf-row{display:flex;justify-content:space-between;font-size:4.5px;line-height:1.45;border-bottom:.5px solid var(--ink)}
  .nf-row.bold{border-bottom:1.5px solid var(--ink)}
  .nf-dv{text-align:right;font-size:4.5px;line-height:1.5}
  .nf-note{font-size:4px;line-height:1.2;margin-top:2px;border-bottom:2px solid var(--ink);padding-bottom:2px}

  .maker{position:absolute;font-size:10.5px;line-height:1.25;color:var(--maroon);white-space:nowrap}
  .maker strong{display:block;color:var(--navy);font-weight:700;letter-spacing:.3px}
  .maker .web{display:block;color:var(--maroon);font-weight:700}

  .ingredients{position:absolute;font-size:9.6px;line-height:1.38;color:var(--ink);white-space:nowrap}
  .ingredients h4{margin:0 0 2px;font-size:9.6px;font-weight:700;color:var(--navy)}
  .ingredients p{margin:0}
  .exp{position:absolute;font-size:9px;font-weight:700;color:var(--ink);transform:rotate(-90deg);transform-origin:left top}

  .title-serif{position:absolute;transform:translateX(-50%);white-space:nowrap;font-family:"Playfair Display",serif;font-weight:900;line-height:1;text-align:center}
  .title-script{position:absolute;transform:translateX(-50%);white-space:nowrap;font-family:"Mr Dafoe",cursive;color:var(--chili);line-height:1}
  .title-sub{position:absolute;transform:translateX(-50%);white-space:nowrap;font-family:"Montserrat",sans-serif;color:var(--chili);font-weight:500;line-height:1}
  .vegan{position:absolute;font-family:"Playfair Display",serif;font-weight:800;font-size:21px;line-height:1;color:var(--leaf)}

  .art{position:absolute;border-radius:8px}
  .art-leaf{background:radial-gradient(circle,#a9655a 0%,rgba(122,52,44,.25) 65%,transparent 100%)}
  .art-berry{background:radial-gradient(circle,#4a4a4a 0%,rgba(60,60,60,.3) 62%,transparent 100%)}
  .art-chili{background:linear-gradient(160deg,transparent 10%,#2a2a2a 35%,#c8201f 55%,#9e1616 75%,transparent 95%);opacity:.85}

  .ribbon{fill:none;stroke:var(--maroon);stroke-width:20}
  .ribbon-text{font-family:"Playfair Display",serif;font-weight:800;font-size:14px;fill:var(--ribbon-text);letter-spacing:1px}
  .volume{font-family:"Montserrat",sans-serif;font-weight:600;font-size:16px;fill:var(--navy)}
</style>
</head>
<body>

<svg width="0" height="0" style="position:absolute" aria-hidden="true">
  <defs>
    <radialGradient id="kraft-fill" cx="50%" cy="50%" r="60%">
      <stop offset="0" stop-color="#ffffff"/>
      <stop offset=".32" stop-color="#fbf6ef"/>
      <stop offset=".7" stop-color="#d8b890"/>
      <stop offset="1" stop-color="#b48658"/>
    </radialGradient>
  </defs>
</svg>

<!-- Maple syrup -->
<section class="label" style="left:64px;top:36px;width:572px;height:306px">
  <svg class="label-shape" width="572" height="306" viewBox="0 0 572 306">
    <path class="outline" fill="url(#kraft-fill)" d="M0,46 H150 C192,46 200,0 288,0 C376,0 384,46 426,46 H572 V264 H426 C384,264 376,306 288,306 C200,306 192,264 150,264 H0 Z"/>
    <path id="vol-maple" d="M224,282 Q288,302 352,282" fill="none"/>
    <text class="volume"><textPath href="#vol-maple" startOffset="50%" text-anchor="middle">8 fl oz/236 ml</textPath></text>
  </svg>
  <div class="nutrition" style="left:14px;top:66px;width:118px;height:148px">
    <h3>NUTRITION FACTS</h3>
    <div class="nf-head"><span>Serving size</span><span>Servings per container</span></div>
    <div class="nf-row bold"><span>Amount per serving</span><span>Calories</span></div>
    <div class="nf-dv">% Daily Value</div>
    <div class="nf-row"><span>Total fat</span><span>g %</span></div>
    <div class="nf-row"><span>Saturated fat</span><span>g %</span></div>
    <div class="nf-row"><span>Cholesterol</span><span>g %</span></div>
    <div class="nf-row"><span>Sodium</span><span>g %</span></div>
    <div class="nf-row"><span>Total carbohydrate</span><span>g %</span></div>
    <div class="nf-row"><span>Dietary fiber</span><span>g %</span></div>
    <div class="nf-row"><span>Sugar</span><span>g %</span></div>
    <div class="nf-row bold"><span>Protein</span><span>g %</span></div>
    <div class="nf-row"><span>Vitamin A · Vitamin C</span><span>%</span></div>
    <div class="nf-row"><span>Calcium · Iron</span><span>%</span></div>
    <div class="nf-note">Percent Daily Values are based on a 2,000 calorie diet.</div>
  </div>
  <div class="brand" style="left:288px;top:10px"><span class="brand-dot"></span><div class="brand-name">FENWICK HOLLOW<br>FARM</div></div>
  <div class="title-serif" style="left:288px;top:112px;font-size:34px;color:var(--maroon)">IRON OATH</div>
  <div class="title-serif" style="left:288px;top:150px;font-size:28px;color:var(--navy)">MAPLE SYRUP</div>
  <div class="art art-leaf" role="img" aria-label="Engraved maple leaf illustration" style="left:246px;top:182px;width:84px;height:80px"></div>
  <div class="maker" style="left:14px;top:228px">Made in Maine by:<strong>FENWICK HOLLOW FARM</strong><span class="web">www.fenwickhollowfarm.com</span></div>
  <div class="ingredients" style="left:446px;top:64px"><h4>Ingredients:</h4><p>Untiaece peruptatem<br>rem. Hitem fuga. Me<br>doloris sequosti ipsam<br>ea denitem. At estinver-<br>at. Laborer ovidel illa di<br>aliquibus, voluptate<br>natiber ferunt volent<br>apelique nonest abo.</p></div>
  <div class="exp" style="left:548px;top:256px">Exp:</div>
</section>

<!-- Kombucha -->
<section class="label" style="left:514px;top:288px;width:652px;height:348px">
  <svg class="label-shape" width="652" height="348" viewBox="0 0 652 348">
    <path class="outline" fill="url(#kraft-fill)" d="M0,52 H190 C236,52 244,0 326,0 C408,0 416,52 462,52 H652 V300 H462 C416,300 408,348 326,348 C244,348 236,300 190,300 H0 Z"/>
    <path id="ribbon-organic" class="ribbon" d="M156,132 Q222,128 290,104"/>
    <text class="ribbon-text" dominant-baseline="central"><textPath href="#ribbon-organic" startOffset="52%" text-anchor="middle">ORGANIC</textPath></text>
    <path id="vol-kombucha" d="M258,324 Q326,344 394,324" fill="none"/>
    <text class="volume"><textPath href="#vol-kombucha" startOffset="50%" text-anchor="middle">12 fl oz/355 ml</textPath></text>
  </svg>
  <div class="nutrition" style="left:16px;top:72px;width:136px;height:170px">
    <h3 style="font-size:17px">NUTRITION FACTS</h3>
    <div class="nf-head"><span>Serving size</span><span>Servings per container</span></div>
    <div class="nf-row bold"><span>Amount per serving</span><span>Calories</span></div>
    <div class="nf-dv">% Daily Value</div>
    <div class="nf-row"><span>Total fat</span><span>g %</span></div>
    <div class="nf-row"><span>Saturated fat</span><span>g %</span></div>
    <div class="nf-row"><span>Cholesterol</span><span>g %</span></div>
    <div class="nf-row"><span>Sodium</span><span>g %</span></div>
    <div class="nf-row"><span>Total carbohydrate</span><span>g %</span></div>
    <div class="nf-row"><span>Dietary fiber</span><span>g %</span></div>
    <div class="nf-row"><span>Sugar</span><span>g %</span></div>
    <div class="nf-row bold"><span>Protein</span><span>g %</span></div>
    <div class="nf-row"><span>Vitamin A · Vitamin C</span><span>%</span></div>
    <div class="nf-row"><span>Calcium · Iron</span><span>%</span></div>
    <div class="nf-note">Percent Daily Values are based on a 2,000 calorie diet.</div>
  </div>
  <div class="brand" style="left:326px;top:12px"><span class="brand-dot"></span><div class="brand-name">FENWICK HOLLOW<br>FARM</div></div>
  <div class="title-serif" style="left:338px;top:134px;font-size:23px;color:var(--maroon)">WILD BLUEBERRY</div>
  <div class="title-serif" style="left:326px;top:160px;font-size:44px;color:var(--navy)">KOMBUCHA</div>
  <div class="art art-berry" role="img" aria-label="Engraved wild blueberry cluster illustration" style="left:282px;top:210px;width:88px;height:94px"></div>
  <div class="maker" style="left:16px;top:252px;font-size:11.5px">Made in Maine by:<strong>FENWICK HOLLOW FARM</strong><span class="web">www.fenwickhollowfarm.com</span></div>
  <div class="ingredients" style="left:509px;top:70px;font-size:10.4px"><h4 style="font-size:10.4px">Ingredients:</h4><p>Untiaece peruptatem<br>rem. Hitem fuga. Me<br>doloris sequosti ipsam<br>ea denitem. At estinver-<br>at. Laborer ovidel illa di<br>aliquibus, voluptate<br>natiber ferunt volent<br>apelique nonest abo.</p></div>
  <div class="exp" style="left:628px;top:290px">Exp:</div>
</section>

<!-- Kimchi -->
<section class="label" style="left:54px;top:578px;width:590px;height:314px">
  <svg class="label-shape" width="590" height="314" viewBox="0 0 590 314">
    <path class="outline" fill="url(#kraft-fill)" d="M0,48 H160 C204,48 212,0 298,0 C384,0 392,48 436,48 H590 V268 H436 C392,268 384,314 298,314 C212,314 204,268 160,268 H0 Z"/>
    <path id="ribbon-traditional" class="ribbon" d="M262,132 Q332,124 402,102"/>
    <text class="ribbon-text" dominant-baseline="central"><textPath href="#ribbon-traditional" startOffset="52%" text-anchor="middle">TRADITIONAL</textPath></text>
    <path id="vol-kimchi" d="M230,292 Q298,314 366,292" fill="none"/>
    <text class="volume"><textPath href="#vol-kimchi" startOffset="50%" text-anchor="middle">8 fl oz/236 ml</textPath></text>
  </svg>
  <div class="nutrition" style="left:16px;top:66px;width:122px;height:154px">
    <h3>NUTRITION FACTS</h3>
    <div class="nf-head"><span>Serving size</span><span>Servings per container</span></div>
    <div class="nf-row bold"><span>Amount per serving</span><span>Calories</span></div>
    <div class="nf-dv">% Daily Value</div>
    <div class="nf-row"><span>Total fat</span><span>g %</span></div>
    <div class="nf-row"><span>Saturated fat</span><span>g %</span></div>
    <div class="nf-row"><span>Cholesterol</span><span>g %</span></div>
    <div class="nf-row"><span>Sodium</span><span>g %</span></div>
    <div class="nf-row"><span>Total carbohydrate</span><span>g %</span></div>
    <div class="nf-row"><span>Dietary fiber</span><span>g %</span></div>
    <div class="nf-row"><span>Sugar</span><span>g %</span></div>
    <div class="nf-row bold"><span>Protein</span><span>g %</span></div>
    <div class="nf-row"><span>Vitamin A · Vitamin C</span><span>%</span></div>
    <div class="nf-row"><span>Calcium · Iron</span><span>%</span></div>
    <div class="nf-note">Percent Daily Values are based on a 2,000 calorie diet.</div>
  </div>
  <div class="brand" style="left:296px;top:10px"><span class="brand-dot"></span><div class="brand-name">FENWICK HOLLOW<br>FARM</div></div>
  <div class="title-script" style="left:292px;top:134px;font-size:72px">Kimchi</div>
  <div class="art art-chili" role="img" aria-label="Red Korean chili pepper crossed with black chopsticks" style="left:216px;top:200px;width:130px;height:72px"></div>
  <div class="vegan" style="left:350px;top:232px">vegan</div>
  <div class="maker" style="left:15px;top:230px">Made in Maine by:<strong>FENWICK HOLLOW FARM</strong><span class="web">www.fenwickhollowfarm.com</span></div>
  <div class="ingredients" style="left:461px;top:64px"><h4>Ingredients:</h4><p>Untiaece peruptatem<br>rem. Hitem fuga. Me<br>doloris sequosti ipsam<br>ea denitem. At estinver-<br>at. Laborer ovidel illa di<br>aliquibus, voluptate<br>natiber ferunt volent<br>apelique nonest abo.</p></div>
  <div class="exp" style="left:566px;top:262px">Exp:</div>
</section>

<!-- Pomrak sauce -->
<section class="label" style="left:512px;top:832px;width:604px;height:324px">
  <svg class="label-shape" width="604" height="324" viewBox="0 0 604 324">
    <path class="outline" fill="url(#kraft-fill)" d="M0,48 H168 C212,48 220,0 304,0 C388,0 396,48 440,48 H604 V276 H440 C396,276 388,324 304,324 C220,324 212,276 168,276 H0 Z"/>
    <path id="vol-pomrak" d="M236,298 Q304,318 372,298" fill="none"/>
    <text class="volume"><textPath href="#vol-pomrak" startOffset="50%" text-anchor="middle">8 fl oz/236 ml</textPath></text>
  </svg>
  <div class="nutrition" style="left:14px;top:66px;width:126px;height:158px">
    <h3 style="font-size:16px">NUTRITION FACTS</h3>
    <div class="nf-head"><span>Serving size</span><span>Servings per container</span></div>
    <div class="nf-row bold"><span>Amount per serving</span><span>Calories</span></div>
    <div class="nf-dv">% Daily Value</div>
    <div class="nf-row"><span>Total fat</span><span>g %</span></div>
    <div class="nf-row"><span>Saturated fat</span><span>g %</span></div>
    <div class="nf-row"><span>Cholesterol</span><span>g %</span></div>
    <div class="nf-row"><span>Sodium</span><span>g %</span></div>
    <div class="nf-row"><span>Total carbohydrate</span><span>g %</span></div>
    <div class="nf-row"><span>Dietary fiber</span><span>g %</span></div>
    <div class="nf-row"><span>Sugar</span><span>g %</span></div>
    <div class="nf-row bold"><span>Protein</span><span>g %</span></div>
    <div class="nf-row"><span>Vitamin A · Vitamin C</span><span>%</span></div>
    <div class="nf-row"><span>Calcium · Iron</span><span>%</span></div>
    <div class="nf-note">Percent Daily Values are based on a 2,000 calorie diet.</div>
  </div>
  <div class="brand" style="left:304px;top:10px"><span class="brand-dot"></span><div class="brand-name">FENWICK HOLLOW<br>FARM</div></div>
  <div class="title-script" style="left:304px;top:108px;font-size:66px">Pomrak</div>
  <div class="title-sub" style="left:318px;top:178px;font-size:22px">SAUCE</div>
  <div class="art art-chili" role="img" aria-label="Red Korean chili pepper crossed with black chopsticks" style="left:238px;top:206px;width:130px;height:74px"></div>
  <div class="maker" style="left:14px;top:234px">Made in Maine by:<strong>FENWICK HOLLOW FARM</strong><span class="web">www.fenwickhollowfarm.com</span></div>
  <div class="ingredients" style="left:472px;top:64px"><h4>Ingredients:</h4><p>Untiaece peruptatem<br>rem. Hitem fuga. Me<br>doloris sequosti ipsam<br>ea denitem. At estinver-<br>at. Laborer ovidel illa di<br>aliquibus, voluptate<br>natiber ferunt volent<br>apelique nonest abo.</p></div>
  <div class="exp" style="left:580px;top:270px">Exp:</div>
</section>

</body>
</html>
```